Could You Go Solo Tomorrow? Podcast

We need a "Podcast Cover" for inclusion on Tunora and wavepocket along with a matching or complimentary banner to be included on a landing page which will be hosted on Castlyn (a Castlyn template). The Podcast is called the "Could You Go Solo Tomorrow?" Podcast and has a tag line of "Hear it first, then jump".

I've included an image for a bit of inspiration that shows a person ready to leap into the unknown which, in our podcast, is like a metaphor for launching a business. You may use the photo in your design if you wish or do something completely different including "cartoon" characters or simply text.

Target Market(s)

People who are thinking about starting a new business or buying an existing business and whom have never owned a business before.

Industry/Entity Type

Startup

Font styles to use
Sans Serif

Colors

Designer to choose colors to be used in the design.

Requirements
Must have
• incorporate the "Hear it first, then jump" tagline.

```html
<!DOCTYPE html>
<html lang="en">
<head>
<meta charset="utf-8">
<title>Could You Go Solo Tomorrow? Podcast Cover</title>
<link rel="stylesheet" href="https://fonts.googleapis.com/css2?family=Work+Sans:wght@700&family=Rubik:wght@900&family=Bebas+Neue&display=swap">
<style>
  :root {
    --sky-top: #f7a23a;
    --sky-mid: #fbb349;
    --sky-glow: #fde7a0;
    --sky-low: #e88a2c;
    --ridge: #2a1408;
    --white: #ffffff;
    --leap-yellow: #f7ef13;
    --band-yellow: #efe12a;
    --ink: #111111;
  }
  * { margin: 0; padding: 0; box-sizing: border-box; }
  html, body {
    width: 1200px;
    height: 1200px;
    overflow: hidden;
    background: var(--band-yellow);
  }
  .cover {
    position: relative;
    width: 1200px;
    height: 1200px;
    overflow: hidden;
  }
  .cover__scene {
    position: absolute;
    inset: 0 0 313px 0;
    background:
      radial-gradient(circle at 50% 33%, var(--sky-glow) 0, var(--sky-mid) 22%, transparent 55%),
      linear-gradient(180deg, var(--sky-top) 0%, var(--sky-mid) 45%, var(--sky-low) 75%, var(--ridge) 100%);
  }
  .cover__tagline {
    position: absolute;
    left: 0;
    top: 0;
    width: 1200px;
    height: 887px;
  }
  .tagline__lead {
    font-family: "Work Sans", sans-serif;
    font-weight: 700;
    font-size: 120px;
    fill: var(--white);
  }
  .tagline__accent {
    font-family: "Rubik", sans-serif;
    font-weight: 900;
    font-size: 156px;
    fill: var(--leap-yellow);
  }
  .cover__band {
    position: absolute;
    left: 0;
    right: 0;
    bottom: 0;
    height: 313px;
    background: var(--band-yellow);
  }
  .band__title {
    position: absolute;
    left: 49px;
    top: 88px;
    width: 1104px;
    height: 120px;
  }
  .band__title text {
    font-family: "Bebas Neue", sans-serif;
    font-size: 150px;
    fill: var(--ink);
  }
</style>
</head>
<body>
  <main class="cover">
    <div class="cover__scene" role="img" aria-label="Photograph of a sunset sky with a silhouetted person leaping across a gap between two dark rocky cliffs"></div>

    <svg class="cover__tagline" viewBox="0 0 1200 887" aria-label="Hear it first, then jump">
      <text class="tagline__lead" x="173" y="693" textLength="834" lengthAdjust="spacingAndGlyphs">HEAR IT FIRST</text>
      <text class="tagline__accent" x="253" y="833" textLength="700" lengthAdjust="spacingAndGlyphs">THEN JUMP</text>
    </svg>

    <section class="cover__band">
      <svg class="band__title" viewBox="0 0 1104 120" aria-label="Could You Go Solo Tomorrow?">
        <text x="0" y="112" textLength="1104" lengthAdjust="spacingAndGlyphs">COULD YOU GO SOLO TOMORROW?</text>
      </svg>
    </section>
  </main>
</body>
</html>
```